Sales Flyer for Outdoor Kitchens

Looks to have a trifold flyer designed based off website content / projects. Use www.brickleafyardworks.com for content

```html
<!DOCTYPE html>
<html lang="en">
<head>
<meta charset="utf-8">
<title>Brickleaf Yardworks Trifold</title>
<link rel="stylesheet" href="https://fonts.googleapis.com/css2?family=Montserrat:wght@400;500;600;700;800&family=Yellowtail&display=swap">
<style>
:root{
  --blue:#1a6fc4;
  --blue-light:#3aa6ea;
  --green:#2fae45;
  --green-dark:#1d8a33;
  --ink:#1b1b1b;
  --paper:#ffffff;
  --stage:#e4e4e4;
}
*{box-sizing:border-box;margin:0;padding:0}
html,body{width:803px;height:1200px;overflow:hidden;background:var(--stage)}
body{position:relative;font-family:"Montserrat",sans-serif;color:var(--ink)}
.spread{position:absolute;left:20px;width:763px;height:540px;background:var(--paper);overflow:hidden;box-shadow:0 3px 10px rgba(0,0,0,.25)}
.spread--outside{top:40px}
.spread--inside{top:620px}
.shapes{position:absolute;inset:0}
.abs{position:absolute}
.photo{position:absolute}

/* outside: about panel */
.about{left:24px;top:18px;width:210px}
.eyebrow{font-size:7px;font-weight:600;color:var(--green)}
.section-title{font-size:13px;font-weight:800;color:var(--ink);display:flex;align-items:center;gap:6px;margin-top:2px}
.section-title .accent{color:var(--blue)}
.section-title::after{content:"";width:26px;height:2px;background:var(--blue)}
.body-copy{font-size:7.6px;line-height:1.32;margin-top:8px;color:#222}
.rule{height:1px;background:#cfcfcf;margin:12px 0 10px}

/* outside: contact panel */
.contact{left:270px;top:18px;width:224px;color:#fff}
.pill{display:block;background:var(--blue-light);border-radius:12px;text-align:center;font-size:12px;font-weight:700;padding:4px 0;color:#fff}
.phone{display:flex;align-items:center;gap:6px;font-size:22px;font-weight:700;margin-top:10px}
.contact-line{display:flex;align-items:flex-start;gap:7px;font-size:8px;line-height:1.3;margin-top:6px}
.contact-line svg{flex:none;margin-top:1px}
.brand-name{position:absolute;text-align:center;font-weight:700;letter-spacing:1px;line-height:1.1}
.brand-name--contact{left:254px;width:255px;top:200px;color:#fff;font-size:24px}
.brand-name--cover{left:509px;width:254px;top:28px;color:var(--blue);font-size:24px}

/* outside: cover */
.cover-title{left:509px;width:254px;top:352px;text-align:center}
.cover-script{font-family:"Yellowtail",cursive;color:var(--green);font-size:36px;line-height:1}
.cover-line1{font-weight:800;color:var(--blue);font-size:25px;line-height:1.05}
.cover-line2{font-weight:800;color:var(--ink);font-size:24px;line-height:1.05}
.cover-line3{font-weight:500;color:var(--ink);font-size:22px;line-height:1.1}
.cover-url{left:509px;width:254px;top:505px;text-align:center;color:#fff;font-weight:700;font-size:13px}

/* inside: services */
.tab{left:26px;top:45px;width:220px;height:40px;background:var(--blue);border-radius:18px 18px 0 0;color:#fff;font-weight:800;font-size:20px;text-align:center;line-height:42px}
.process-title{left:262px;top:18px;width:220px;text-align:center;color:var(--green);font-weight:800;font-size:15px;line-height:1.05}
.service-card{position:absolute;width:170px}
.service-card .thumb{width:170px;height:76px;border-radius:12px}
.service-name{font-size:10.5px;font-weight:800;color:var(--green);margin-top:5px;line-height:1.1}
.service-text{font-size:7.4px;line-height:1.3;color:#333;margin-top:1px}

/* inside: expertise panel */
.expertise{left:525px;top:20px;width:222px;color:#fff}
.outline-pill{display:block;border:2px solid #fff;background:var(--green-dark);border-radius:14px;text-align:center;font-weight:700;font-size:12px;padding:3px 0}
.item-head{font-size:8px;font-weight:700;margin-top:10px}
.item-text{font-size:6.8px;line-height:1.3}
.lead{font-size:8px;font-weight:700;margin-top:10px}
.white-rule{height:2px;background:#fff;margin:14px 0 12px}
</style>
</head>
<body>

<!-- OUTSIDE SPREAD -->
<section class="spread spread--outside">
  <svg class="shapes" viewBox="0 0 763 540" width="763" height="540">
    <defs>
      <linearGradient id="gPav" x1="0" y1="0" x2="1" y2="1"><stop offset="0" stop-color="#8d8a82"/><stop offset=".5" stop-color="#a0693e"/><stop offset="1" stop-color="#5c5a52"/></linearGradient>
      <linearGradient id="gRoof" x1="0" y1="0" x2="0" y2="1"><stop offset="0" stop-color="#5e8a3e"/><stop offset=".5" stop-color="#9b6a3e"/><stop offset="1" stop-color="#6d8f4a"/></linearGradient>
    </defs>
    <rect x="254" y="0" width="255" height="325" fill="var(--blue)"/>
    <path d="M509,140 Q640,95 763,112 L763,128 Q640,112 509,156Z" fill="var(--blue)"/>
    <path d="M509,152 Q640,108 763,124 L763,322 L509,322Z" fill="url(#gRoof)" role="img" aria-label="Photo of a cedar pavilion with fire pit and seating on a lawn"/>
    <rect x="254" y="325" width="509" height="7" fill="var(--blue)"/>
    <rect x="254" y="336" width="509" height="3" fill="var(--blue-light)"/>
    <path d="M254,540 L254,500 Q520,515 763,455 L763,540Z" fill="var(--green)"/>
    <path d="M0,330 Q190,318 300,540 L0,540Z" fill="var(--blue)"/>
    <path d="M0,346 Q170,336 280,540 L0,540Z" fill="url(#gPav)" role="img" aria-label="Photo of a covered patio with white posts, stone columns and outdoor dining"/>
    <circle cx="330" cy="455" r="102" fill="var(--blue)"/>
    <circle cx="330" cy="455" r="94" fill="#c9c2b5" role="img" aria-label="Photo of an open patio room with ceiling fan and concrete floor"/>
  </svg>

  <div class="abs about">
    <p class="eyebrow">What we do</p>
    <h2 class="section-title">WHO WE ARE</h2>
    <p class="body-copy">With over a decade of experience in the industry, Daniel Hale, the owner and operator of Brickleaf, has become a well-known name in the Fairview area. His passion for outdoor living spaces, coupled with his keen eye for design and attention to detail, has led him to create some of the most stunning and functional outdoor spaces for his clients.</p>
    <div class="rule"></div>
    <h2 class="section-title">OUR <span class="accent">MISSION</span></h2>
    <p class="body-copy">At Brickleaf Yardworks, our mission is to redefine outdoor living by blending innovative design with unmatched craftsmanship. We strive to create spaces that not only meet but exceed your expectations. Our goal is to transform your outdoor area into a haven that reflects your personality and provides a seamless connection between nature and your home.</p>
  </div>

  <div class="abs contact">
    <span class="pill">CONTACT</span>
    <p class="phone"><svg width="12" height="18" viewBox="0 0 12 18"><path d="M3,1 L6,1 L6,5 L4,6 Q4,11 7,13 L9,11 L11,13 L11,16 Q3,17 1,8 Q1,3 3,1Z" fill="#fff"/></svg>555-014-2290</p>
    <p class="contact-line"><svg width="8" height="11" viewBox="0 0 8 11"><path d="M4,0 A4,4 0 0 1 8,4 Q8,7 4,11 Q0,7 0,4 A4,4 0 0 1 4,0Z" fill="#fff"/><circle cx="4" cy="4" r="1.6" fill="var(--blue)"/></svg>4820 Cedar Mill Rd Ste 210<br>Fairview, 75069, US</p>
    <p class="contact-line"><svg width="9" height="9" viewBox="0 0 9 9"><circle cx="4.5" cy="4.5" r="4.5" fill="#fff"/><rect x="2" y="3" width="5" height="3.4" fill="var(--blue)"/></svg>hello@brickleafyardworks.com</p>
    <p class="contact-line"><svg width="9" height="9" viewBox="0 0 9 9"><circle cx="4.5" cy="4.5" r="4.5" fill="#fff"/><circle cx="4.5" cy="4.5" r="2.2" fill="none" stroke="var(--blue)" stroke-width=".8"/></svg>www.brickleafyardworks.com</p>
  </div>

  <p class="brand-name brand-name--contact">BRICKLEAF<br>YARDWORKS</p>
  <p class="brand-name brand-name--cover">BRICKLEAF<br>YARDWORKS</p>

  <div class="abs cover-title">
    <p class="cover-script">Create</p>
    <p class="cover-line1">YOUR DREAM</p>
    <p class="cover-line2">Backyard</p>
    <p class="cover-line3">With Us</p>
  </div>
  <p class="abs cover-url">brickleafyardworks.com</p>
</section>

<!-- INSIDE SPREAD -->
<section class="spread spread--inside">
  <svg class="shapes" viewBox="0 0 763 540" width="763" height="540">
    <defs>
      <linearGradient id="gHouse" x1="0" y1="0" x2="1" y2="0"><stop offset="0" stop-color="#c9d3dc"/><stop offset=".5" stop-color="#e8ecef"/><stop offset="1" stop-color="#b4a58a"/></linearGradient>
      <linearGradient id="gKitchen" x1="0" y1="0" x2="1" y2="1"><stop offset="0" stop-color="#9ec3e6"/><stop offset=".5" stop-color="#c7b9a3"/><stop offset="1" stop-color="#6e6a63"/></linearGradient>
    </defs>
    <rect x="0" y="0" width="509" height="120" fill="url(#gHouse)" role="img" aria-label="Photo of a white two-storey home with large windows"/>
    <rect x="28" y="82" width="452" height="440" rx="22" fill="#fff" stroke="var(--blue)" stroke-width="3"/>
    <circle cx="500" cy="505" r="128" fill="var(--blue)"/>
    <circle cx="500" cy="505" r="120" fill="url(#gKitchen)" role="img" aria-label="Photo of a stone outdoor kitchen with stainless grill"/>
    <rect x="509" y="0" width="254" height="540" fill="var(--green)"/>
  </svg>

  <div class="abs tab">OUR SERVICES</div>
  <p class="abs process-title">EFFECTIVE<br>PROCESS FOR GREAT<br>OUTCOMES</p>

  <div class="service-card" style="left:58px;top:100px">
    <div class="thumb" role="img" aria-label="Photo of a brick outdoor kitchen with built-in grill" style="background:linear-gradient(135deg,#5f8d3e,#8a5b3c,#6b6b6b)"></div>
    <p class="service-name">OUTDOOR KITCHENS</p>
    <p class="service-text">Culinary Excellence in Your Outdoor Sanctuary Welcome to Outdoor</p>
  </div>
  <div class="service-card" style="left:58px;top:240px">
    <div class="thumb" role="img" aria-label="Photo of a white gabled pavilion over a patio" style="background:linear-gradient(135deg,#7fa35a,#e3ddd2,#8a5b3c)"></div>
    <p class="service-name">PAVILIONS, PATIOS &amp;<br>PERGOLAS</p>
    <p class="service-text">Pergolas and Patio Covers – Shaping Serenity in Your</p>
  </div>
  <div class="service-card" style="left:58px;top:385px">
    <div class="thumb" role="img" aria-label="Photo of a round stone fire pit lit at dusk" style="background:linear-gradient(135deg,#3f5a3a,#c98a4a,#8a7465)"></div>
    <p class="service-name">FIRE PITS</p>
    <p class="service-text">Elevate Your Outdoor Space with Unique Fire Features At</p>
  </div>
  <div class="service-card" style="left:278px;top:100px">
    <div class="thumb" role="img" aria-label="Photo of a backyard swimming pool beside a white house" style="background:linear-gradient(135deg,#c7d6e2,#4fb6e3,#8aa079)"></div>
    <p class="service-name">POOLS</p>
    <p class="service-text">Our expert team will create a customized plan that brings together your</p>
  </div>
  <div class="service-card" style="left:278px;top:240px">
    <div class="thumb" role="img" aria-label="Photo of lush landscaped garden beds" style="background:linear-gradient(135deg,#1f3d22,#4c8a3a,#1b2c1c)"></div>
    <p class="service-name">LANDSCAPING &amp;<br>LIGHTING</p>
    <p class="service-text">Design a captivating backyard oasis with our landscaping and lighting service, harmonizing</p>
  </div>

  <div class="abs expertise">
    <span class="outline-pill">OUR EXPERTISE</span>
    <p class="item-head">Outdoor Living Spaces:</p>
    <p class="item-text">Our team specializes in designing outdoor living spaces that harmonize with your lifestyle, providing the perfect backdrop for relaxation and entertainment.</p>
    <p class="item-head">Patios:</p>
    <p class="item-text">Elevate your outdoor experience with a well-designed patio that seamlessly extends your living space into the open air. We tailor our designs to your unique preferences.</p>
    <p class="item-head">Pergolas:</p>
    <p class="item-text">Embrace the allure of outdoor elegance with our custom pergola designs. Whether you seek a cozy nook or a captivating focal point, our pergolas are crafted to elevate your outdoor aesthetic.</p>
    <p class="item-head">Fire Features:</p>
    <p class="item-text">Our fire features combine style with ambiance. We offer everything from eye-catching fireplaces to fire pits that promise to beckon a crowd.</p>
    <div class="white-rule"></div>
    <span class="outline-pill">OUR VALUES</span>
    <p class="lead">We perform complete turnkey services</p>
    <p class="item-head">Passion:</p>
    <p class="item-text">We're driven by a deep passion for outdoor design, and it is reflected in every project. Our commitment to excellence is fueled by our genuine love for creating outdoor spaces that enhance the quality of life.</p>
    <p class="item-head">Attention to Detail:</p>
    <p class="item-text">Every element matters. We approach each design with meticulous attention to detail, ensuring that every aspect contributes to the overall aesthetic and functionality of your outdoor space.</p>
    <p class="item-head">Client-Centric Approach:</p>
    <p class="item-text">Your vision is our priority. We believe in collaborative design, working closely with you to understand your preferences and lifestyle, and translating them into a personalized outdoor oasis.</p>
  </div>
</section>

</body>
</html>
```